Flyer for Pharmacy/Medical Convention

Tri-fold flyer for pharmacy/medical convention. The inside of the flyer we would like to look like a venn diagram, possibly using an image similar to our blue logo

Copy write will be submitted when a design is chosen

there will be a flap about educational features, one about supplements an automated recommendations, and a flap about a computer platform to manage patients

Target Market(s)

Pharmacists and Medical Providers

Industry/Entity Type

Supplement

Colors

Designer to choose colors to be used in the design.

Requirements
Must have
• color scheme similar to logos and or label design attached

```html
<!DOCTYPE html>
<html lang="en">
<head>
<meta charset="utf-8">
<title>Pharmacy/Medical Convention – Tri-fold Outside</title>
<link href="https://fonts.googleapis.com/css2?family=Montserrat:wght@300;400;600;700&family=Nunito+Sans:wght@300;400&display=swap" rel="stylesheet">
<style>
  :root {
    --backdrop: #2b2b2d;
    --paper: #ffffff;
    --ink: #2a2a2a;
    --navy: #1d2478;
    --blue-deep: #2c3d9c;
    --blue-mid: #3f63b8;
    --blue-light: #5a8fd0;
    --red: #d4202a;
    --red-light: #f1584a;
  }
  * { margin: 0; padding: 0; box-sizing: border-box; }
  html, body { width: 1200px; height: 923px; overflow: hidden; background: var(--backdrop); }
  .canvas { position: relative; width: 1200px; height: 923px; }
  .artwork { position: absolute; inset: 0; }

  .panel-heading {
    position: absolute; left: 104px;
    font-family: "Montserrat", sans-serif; font-weight: 400;
    font-size: 18.5px; line-height: 22px; color: #111; letter-spacing: -0.3px;
  }
  .panel-heading b { font-weight: 700; }
  .panel-heading::after {
    content: ""; position: absolute; left: 0; top: 25px; width: 100px; height: 3px;
    background: linear-gradient(90deg, var(--navy), var(--blue-light));
  }
  .heading-one { top: 88px; }
  .heading-two { top: 464px; left: 103px; }

  .panel-copy {
    position: absolute; left: 103px; width: 294px;
    font-family: "Nunito Sans", sans-serif; font-weight: 400;
    color: var(--ink); font-size: 13.3px; line-height: 15.8px;
  }
  .copy-one { top: 140px; }
  .copy-two { top: 345px; }
  .copy-three { top: 517px; }
  .copy-four { top: 722px; }

  .event-title {
    position: absolute; left: 420px; top: 596px; width: 350px; text-align: center;
    font-family: "Montserrat", sans-serif; font-weight: 700; color: #fff;
    font-size: 25.5px; line-height: 34px; letter-spacing: 0.2px;
  }
  .contact-list { position: absolute; left: 470px; top: 690px; list-style: none; }
  .contact-list li {
    display: flex; align-items: center; height: 34px; margin-bottom: 12.5px;
    font-family: "Montserrat", sans-serif; font-weight: 400; color: #fff;
    font-size: 15px; letter-spacing: 2.6px;
  }
  .contact-list li.phone { letter-spacing: 3.6px; }
  .contact-list svg { width: 34px; height: 34px; margin-right: 14px; flex: none; }

  .brand {
    position: absolute; left: 790px; top: 699px; width: 330px; text-align: center;
    font-family: "Montserrat", sans-serif; font-weight: 700; color: var(--navy);
  }
  .brand-name { font-size: 42px; letter-spacing: 1px; line-height: 50px; }
  .brand-line { font-size: 22px; line-height: 28px; margin-top: 39px; }
</style>
</head>
<body>
<div class="canvas">
  <svg class="artwork" width="1200" height="923" viewBox="0 0 1200 923">
    <defs>
      <linearGradient id="panelBlue" x1="0" y1="0" x2="0.3" y2="1">
        <stop offset="0" stop-color="#5a8fd0"/>
        <stop offset="0.5" stop-color="#3f63b8"/>
        <stop offset="1" stop-color="#3340a0"/>
      </linearGradient>
      <linearGradient id="waveBlue" x1="0" y1="0" x2="1" y2="0">
        <stop offset="0" stop-color="#2b3ea0"/>
        <stop offset="1" stop-color="#4a78c8"/>
      </linearGradient>
      <linearGradient id="hallTones" x1="0" y1="0" x2="1" y2="1">
        <stop offset="0" stop-color="#2c3a66"/>
        <stop offset="0.45" stop-color="#9a6f5a"/>
        <stop offset="0.75" stop-color="#6d6f80"/>
        <stop offset="1" stop-color="#2a2c38"/>
      </linearGradient>
      <linearGradient id="ringRed" x1="0" y1="0" x2="1" y2="1">
        <stop offset="0" stop-color="#f1584a"/>
        <stop offset="1" stop-color="#c81a24"/>
      </linearGradient>
      <linearGradient id="classroomTones" x1="0" y1="0" x2="1" y2="1">
        <stop offset="0" stop-color="#e8e8ea"/>
        <stop offset="1" stop-color="#9c8a80"/>
      </linearGradient>
      <linearGradient id="staffTones" x1="0" y1="0" x2="1" y2="1">
        <stop offset="0" stop-color="#c9dbe8"/>
        <stop offset="1" stop-color="#f2f4f6"/>
      </linearGradient>
    </defs>

    <rect class="sheet" x="68" y="38" width="1066" height="830" fill="var(--paper)"/>
    <rect class="middle-panel" x="420" y="38" width="714" height="830" fill="url(#panelBlue)"/>

    <path class="right-panel" d="M770,868 L770,582 Q950,640 1134,584 L1134,868 Z" fill="var(--paper)"/>
    <path class="wave-band" d="M650,470 Q860,600 1134,528 L1134,584 Q950,640 770,582 Q700,540 650,470 Z" fill="url(#waveBlue)"/>

    <path class="hall-photo" role="img" aria-label="Photo: speaker presenting to a large conference audience"
          d="M586,38 L1134,38 L1134,528 Q880,590 690,480 Q560,330 586,38 Z"
          fill="url(#hallTones)" stroke="#dfe6f2" stroke-width="3"/>

    <circle class="ring" cx="596" cy="266" r="129" fill="url(#ringRed)"/>
    <circle class="ring-inner" cx="596" cy="266" r="118" fill="#fff"/>
    <circle class="classroom-photo" role="img" aria-label="Photo: presenter teaching a seminar group"
            cx="596" cy="266" r="114" fill="url(#classroomTones)"/>

    <circle class="ring" cx="636" cy="428" r="97" fill="url(#ringRed)"/>
    <circle class="ring-inner" cx="636" cy="428" r="87" fill="#fff"/>
    <circle class="staff-photo" role="img" aria-label="Photo: smiling medical staff in white coats"
            cx="636" cy="428" r="84" fill="url(#staffTones)"/>
  </svg>

  <h2 class="panel-heading heading-one"><b>YOUR</b> HEADLINE</h2>
  <p class="panel-copy copy-one">Lorem ipsum dolor sit amet, consectetuer adipiscing elit, sed diam nonummy nibh euismod tincidunt ut laoreet dolore magna aliquam erat volutpat. Ut wisi enim ad minim veniam, quis nostrud exerci tation ullamcorper suscipit lobortis nisl ut aliquip ex ea commodo consequat. Duis autem vel eum iriure dolor in hendrerit in vulputate velit esse molestie consequat, vel illum dolore eu feugiat nulla facilisis at vero eros et accumsan et iusto odio dignissim qui blandit praesent luptatum zzril delenit augue duis dolore te feugait nulla facilisi.</p>
  <p class="panel-copy copy-two">Duis autem vel eum iriure dolor in hendrerit in vulputate velit esse molestie consequat, vel illum dolore eu feugiat nulla facilisis at vero eros et accumsan et iusto odio dignissim qui blandit praesent luptatum zzril delenit augue duis dolore te feugait nulla facilisi.</p>

  <h2 class="panel-heading heading-two"><b>YOUR</b> TEXT HERE</h2>
  <p class="panel-copy copy-three">Lorem ipsum dolor sit amet, consectetuer adipiscing elit, sed diam nonummy nibh euismod tincidunt ut laoreet dolore magna aliquam erat volutpat. Ut wisi enim ad minim veniam, quis nostrud exerci tation ullamcorper suscipit lobortis nisl ut aliquip ex ea commodo consequat. Duis autem vel eum iriure dolor in hendrerit in vulputate velit esse molestie consequat, vel illum dolore eu feugiat nulla facilisis at vero eros et accumsan et iusto odio dignissim qui blandit praesent luptatum zzril delenit augue duis dolore te feugait nulla facilisi.</p>
  <p class="panel-copy copy-four">Duis autem vel eum iriure dolor in hendrerit in vulputate velit esse molestie consequat, vel illum dolore eu feugiat nulla facilisis at vero eros et accumsan et iusto odio dignissim qui blandit praesent luptatum zzril delenit augue duis dolore te feugait nulla facilisi.</p>

  <h1 class="event-title">PHARMACY/MEDICAL<br>CONVENTION</h1>

  <ul class="contact-list">
    <li class="phone">
      <svg viewBox="0 0 34 34" aria-hidden="true"><circle cx="17" cy="17" r="15.5" fill="none" stroke="#fff" stroke-width="1.6"/>
        <path d="M12,9 L15,9 L16,13 L14,14.5 Q15.5,18.5 19.5,20 L21,18 L25,19 L25,22 Q24,25 21,25 Q10,23 9,12 Q9,9.5 12,9 Z" fill="none" stroke="#fff" stroke-width="1.5" stroke-linejoin="round"/></svg>
      +00 000 000 0000
    </li>
    <li>
      <svg viewBox="0 0 34 34" aria-hidden="true"><circle cx="17" cy="17" r="15.5" fill="none" stroke="#fff" stroke-width="1.6"/>
        <text x="17" y="23" text-anchor="middle" font-family="Montserrat, sans-serif" font-size="17" fill="#fff">@</text></svg>
      mail@yourwebsite.com
    </li>
    <li>
      <svg viewBox="0 0 34 34" aria-hidden="true"><circle cx="17" cy="17" r="15.5" fill="none" stroke="#fff" stroke-width="1.6"/>
        <g fill="none" stroke="#fff" stroke-width="1.3"><circle cx="17" cy="17" r="9"/><ellipse cx="17" cy="17" rx="4" ry="9"/><line x1="8" y1="17" x2="26" y2="17"/><line x1="9.5" y1="12.5" x2="24.5" y2="12.5"/><line x1="9.5" y1="21.5" x2="24.5" y2="21.5"/></g></svg>
      www.yourwebsite.com
    </li>
  </ul>

  <div class="brand">
    <div class="brand-name">MERIDIAN</div>
    <div class="brand-line">Care Systems</div>
  </div>
</div>
</body>
</html>
```